Cedar Lane Bail Bonds Signboard Ad

I need a signboard ad that will be posted at a jail. We are a bail bond company and we bail people out of jail. The inmate/customer will call our company when they see our signboard ad posted inside a jail. The goal of the signboard ad is to get the attention of a person in custody and to stand out from the competition. The signboard ad is about 5x7. Open to any colors that will make it stand out. The content of the signboard ad must have "Cedar Lane Bail Bonds" and our company phone number: (555) 318-2047. We want to emphasize we can get them out of jail quick and fast, was thinking maybe a catch phrase of "Blast outta Jail" or "Cedar Lane to Freedom". We don't have a logo. I will upload an attachment to show what the competition looks like. As you will see in the upload, my ad will go along with my competition. Also, I'm open to any creative ideas that will make my signboard ad stand out. Thank You.

Target Market(s)

People in jail.

Requirements
Must have
• Cedar Lane Bail Bonds

(555) 318-2047
Nice to have
• I'm open to catch phrases that will get attention, for example "Blast outta Jail" or "Cedar Lane to Freedom". I do not have a company logo, if you can create a company logo, would be nice, was thinking an image of a rocket blasting off, The name of company is Cedar Lane Bail Bonds.

```html
<!DOCTYPE html>
<html lang="en">
<head>
<meta charset="utf-8">
<title>Cedar Lane Bail Bonds — Signboard</title>
<link href="https://fonts.googleapis.com/css2?family=Bebas+Neue&family=Montserrat:wght@700;800&display=swap" rel="stylesheet">
<style>
  :root {
    --page-bg: #f4f5f7;
    --navy-top: #05205a;
    --navy-bottom: #021339;
    --royal: #2a529f;
    --band: #123784;
    --white: #ffffff;
    --silver-light: #ffffff;
    --silver-mid: #c9cbcf;
    --silver-dark: #8d9096;
  }
  * { box-sizing: border-box; margin: 0; padding: 0; }
  html, body {
    width: 800px; height: 1200px; overflow: hidden;
    background: var(--page-bg);
  }
  .signboard {
    position: absolute; left: 40px; top: 343px;
    width: 720px; height: 514px;
    background: var(--royal);
    box-shadow: 0 14px 34px rgba(0,0,0,0.28);
    overflow: hidden;
  }
  .signboard-backdrop { position: absolute; inset: 0; width: 100%; height: 100%; }
  .brand {
    position: absolute; top: 62px; left: 0; right: 0;
    display: flex; justify-content: center; align-items: center; gap: 10px;
    font-family: "Montserrat", sans-serif; font-weight: 800;
    font-size: 24px; color: var(--white); letter-spacing: 0.5px;
  }
  .brand-dot {
    width: 18px; height: 18px; border-radius: 50%; background: var(--white);
  }
  .headline {
    position: absolute; left: 0; right: 0; text-align: center;
    font-family: "Bebas Neue", sans-serif; line-height: 1;
  }
  .headline-main {
    top: 140px; font-size: 130px; letter-spacing: 2px;
    background: linear-gradient(180deg, var(--silver-light) 0%, var(--silver-mid) 45%, var(--silver-dark) 60%, var(--silver-light) 100%);
    -webkit-background-clip: text; background-clip: text; color: transparent;
  }
  .headline-sub {
    top: 268px; font-size: 88px; color: var(--white); letter-spacing: 1px;
  }
  .phone {
    position: absolute; left: 0; right: 0; top: 430px;
    display: flex; justify-content: center; align-items: center; gap: 12px;
    font-family: "Montserrat", sans-serif; font-weight: 800;
    font-size: 52px; color: var(--white); line-height: 1;
  }
  .phone-icon { width: 50px; height: 50px; }
</style>
</head>
<body>
  <main class="signboard">
    <svg class="signboard-backdrop" viewBox="0 0 720 514" preserveAspectRatio="none" aria-hidden="true">
      <defs>
        <linearGradient id="navyFade" x1="0" y1="0" x2="0" y2="1">
          <stop offset="0" stop-color="var(--navy-top)"/>
          <stop offset="1" stop-color="var(--navy-bottom)"/>
        </linearGradient>
      </defs>
      <path d="M0 200 Q360 655 720 200 V214 Q360 660 0 214 Z" fill="var(--band)"/>
      <path d="M0 0 H720 V195 Q360 599 0 195 Z" fill="url(#navyFade)"/>
      <path d="M0 195 Q360 599 720 195" fill="none" stroke="var(--white)" stroke-width="2"/>
    </svg>

    <div class="brand"><span class="brand-dot"></span>Cedar Lane Bail Bonds</div>

    <h1 class="headline headline-main">CEDAR LANE</h1>
    <p class="headline headline-sub">TO FREEDOM</p>

    <p class="phone">
      <svg class="phone-icon" viewBox="0 0 48 48" aria-hidden="true">
        <path d="M12 6 l7 9 -4 5 c3 6 8 11 14 14 l5 -4 9 7 -4 6 c-2 2 -5 3 -8 2 C19 41 8 30 4 18 c-1-3 0-6 2-8 z" fill="var(--white)"/>
        <path d="M28 8 a12 12 0 0 1 12 12 M28 13 a7 7 0 0 1 7 7 M28 18 a2 2 0 0 1 2 2" fill="none" stroke="var(--white)" stroke-width="2" stroke-linecap="round"/>
      </svg>
      (555) 318-2047
    </p>
  </main>
</body>
</html>
```